Design a homepage graphic to show a system journey

We have a software package for parents to update student information and manage school excursions we have attached a concept we like but are open to other ideas so long as they fit the following criteria.
1 It needs to be landscape across the page
2. They are showing a series of processes, each step has its own colour, see below
2.1 The first process is a parent updating their own and students information and approving excursions
2.2 The school then creates and manages the excursion this includes a compliance component
2.3 The school conducts the activity it should show some activity type pictures
2.4 Students return safely to school
3 There can be text boxes within the image to clarify functionality
4. The picture should make anyone watching it understand there is a series of
linked processes the system provides i.e. a journey
There should be the ability to click on each component to link to a specific part of the pager lower down, e.g if the person wanted to look at the school part by clicking on the school it would take them to more information, that information already exists so is not required.
Please review the attached concept diagram and use this a potential guide.
Schools
1 page

```html
<!DOCTYPE html>
<html lang="en">
<head>
<meta charset="utf-8">
<title>System Journey</title>
<link rel="stylesheet" href="https://fonts.googleapis.com/css2?family=Montserrat:wght@700;800&display=swap">
<style>
  :root {
    --title-orange: #fb7a14;
    --road: #34566f;
    --road-edge: #264559;
    --green: #9cc93a;
    --green-light: #c6e28f;
    --orange: #fb7a14;
    --orange-light: #fcc84a;
    --pink: #f27cc0;
    --pink-light: #fdb3de;
    --blue: #4b6fdc;
    --blue-light: #55c2ec;
    --purple: #9045f8;
    --purple-light: #c283fb;
    --cyan: #1bd7fb;
    --cyan-light: #86e8fc;
    --paper: #ffffff;
  }
  html, body {
    margin: 0;
    padding: 0;
    width: 1200px;
    height: 748px;
    overflow: hidden;
    background: var(--paper);
  }
  .journey {
    position: relative;
    width: 1200px;
    height: 748px;
    font-family: "Montserrat", Arial, sans-serif;
  }
  .journey__title {
    position: absolute;
    top: 76px;
    left: 0;
    width: 100%;
    margin: 0;
    text-align: center;
    font-size: 38px;
    font-weight: 800;
    letter-spacing: 0.5px;
    color: var(--title-orange);
  }
  .journey__map {
    position: absolute;
    top: 0;
    left: 0;
  }
  .step-label {
    position: absolute;
    transform: translateX(-50%);
    margin: 0;
    font-size: 15px;
    font-weight: 700;
    line-height: 20px;
    text-align: center;
    white-space: nowrap;
    text-decoration: none;
  }
  .step-label--parent   { left: 155px; top: 556px; color: var(--green); }
  .step-label--student  { left: 328px; top: 342px; color: var(--orange); }
  .step-label--approve  { left: 501px; top: 556px; color: var(--pink); }
  .step-label--manage   { left: 672px; top: 342px; color: var(--blue); }
  .step-label--conduct  { left: 846px; top: 556px; color: var(--purple); }
  .step-label--return   { left: 1019px; top: 342px; color: var(--cyan); }

  .scene {
    position: absolute;
    border-radius: 18px;
  }
  .scene--parent-child {
    left: 89px; top: 187px; width: 100px; height: 174px;
    background: linear-gradient(180deg, #f6c9a8 0%, #c94ce0 45%, #2f4f73 100%);
    opacity: 0.55;
  }
  .scene--teacher-pupils {
    left: 430px; top: 203px; width: 140px; height: 158px;
    background: linear-gradient(180deg, #2b3440 0%, #fbd86e 50%, #f29a6a 100%);
    opacity: 0.5;
  }
  .scene--activity-card {
    left: 779px; top: 235px; width: 134px; height: 109px;
    border-radius: 12px;
    background: linear-gradient(160deg, #9447fa 0%, #8a3ff2 100%);
  }
  .scene--happy-pupil {
    left: 287px; top: 581px; width: 80px; height: 110px;
    background: linear-gradient(180deg, #8a4a2a 0%, #2bb3c8 55%, #2f4f56 100%);
    opacity: 0.45;
  }
  .scene--planning-meeting {
    left: 596px; top: 581px; width: 174px; height: 156px;
    border-radius: 48% 52% 40% 44%;
    background: linear-gradient(180deg, #eef0fd 0%, #d9dcf8 60%, #c7cdf4 100%);
  }
  .scene--school-return {
    left: 952px; top: 574px; width: 248px; height: 172px;
    border-radius: 18px 0 0 0;
    background: linear-gradient(160deg, #f3d2b8 0%, #e7eef0 45%, #a9d4a3 100%);
    opacity: 0.8;
  }
  .step-link { cursor: pointer; }
  .icon { fill: none; stroke: #fff; stroke-width: 2.2; stroke-linecap: round; stroke-linejoin: round; }
</style>
</head>
<body>
<main class="journey">
  <h1 class="journey__title">SYSTEM JOURNEY</h1>

  <div class="scene scene--parent-child" role="img" aria-label="Illustration of a mother standing with her young daughter"></div>
  <div class="scene scene--teacher-pupils" role="img" aria-label="Illustration of a teacher guiding two pupils"></div>
  <div class="scene scene--activity-card" role="img" aria-label="Illustration of a teacher handing a medal to children during an activity"></div>
  <div class="scene scene--happy-pupil" role="img" aria-label="Illustration of a smiling schoolgirl"></div>
  <div class="scene scene--planning-meeting" role="img" aria-label="Illustration of two staff members planning at a table in front of a schedule board"></div>
  <div class="scene scene--school-return" role="img" aria-label="Illustration of pupils walking back to the school building"></div>

  <svg class="journey__map" width="1200" height="748" viewBox="0 0 1200 748" aria-hidden="false">
    <defs>
      <linearGradient id="fill-green" x1="0" y1="0" x2="1" y2="1">
        <stop offset="0" stop-color="#a8d04f"/><stop offset="1" stop-color="var(--green-light)"/>
      </linearGradient>
      <linearGradient id="fill-orange" x1="0" y1="0" x2="1" y2="1">
        <stop offset="0" stop-color="#fb7f18"/><stop offset="1" stop-color="#fcd04e"/>
      </linearGradient>
      <linearGradient id="fill-pink" x1="0" y1="0" x2="1" y2="1">
        <stop offset="0" stop-color="#f783c9"/><stop offset="1" stop-color="#fdbae2"/>
      </linearGradient>
      <linearGradient id="fill-blue" x1="0" y1="0" x2="1" y2="1">
        <stop offset="0" stop-color="#4a76df"/><stop offset="1" stop-color="#57c6ee"/>
      </linearGradient>
      <linearGradient id="fill-purple" x1="0" y1="0" x2="1" y2="1">
        <stop offset="0" stop-color="#9a52f9"/><stop offset="1" stop-color="#cb8ffc"/>
      </linearGradient>
      <linearGradient id="fill-cyan" x1="0" y1="0" x2="1" y2="1">
        <stop offset="0" stop-color="#27d9fb"/><stop offset="1" stop-color="#92ebfc"/>
      </linearGradient>
    </defs>

    <g class="road">
      <path d="M0 376 H155 A86.5 86.5 0 0 1 241.5 462 A86.5 86.5 0 0 0 414.5 462 A86.5 86.5 0 0 1 587.5 462 A86.5 86.5 0 0 0 760.5 462 A86.5 86.5 0 0 1 933.5 462 A86.5 86.5 0 0 0 1020 548.5 H1200"
            fill="none" stroke="var(--road-edge)" stroke-width="42"/>
      <path d="M0 376 H155 A86.5 86.5 0 0 1 241.5 462 A86.5 86.5 0 0 0 414.5 462 A86.5 86.5 0 0 1 587.5 462 A86.5 86.5 0 0 0 760.5 462 A86.5 86.5 0 0 1 933.5 462 A86.5 86.5 0 0 0 1020 548.5 H1200"
            fill="none" stroke="var(--road)" stroke-width="36"/>
      <path d="M6 376 H155 A86.5 86.5 0 0 1 241.5 462 A86.5 86.5 0 0 0 414.5 462 A86.5 86.5 0 0 1 587.5 462 A86.5 86.5 0 0 0 760.5 462 A86.5 86.5 0 0 1 933.5 462 A86.5 86.5 0 0 0 1020 548.5 H1200"
            fill="none" stroke="#fff" stroke-width="4" stroke-dasharray="11 18"/>
    </g>

    <a class="step-link" href="#parent-information" aria-label="Parent information">
      <circle cx="155" cy="462" r="68" fill="var(--green)"/>
      <circle cx="155" cy="462" r="53" fill="url(#fill-green)"/>
      <g class="icon">
        <circle cx="143" cy="447" r="9"/><path d="M128 490 v-18 a15 12 0 0 1 30 0 v18"/>
        <circle cx="168" cy="447" r="9"/><path d="M153 490 v-18 a15 12 0 0 1 30 0 v18"/>
      </g>
    </a>
    <a class="step-link" href="#student-information" aria-label="Student information">
      <circle cx="328" cy="462" r="68" fill="var(--orange)"/>
      <circle cx="328" cy="462" r="53" fill="url(#fill-orange)"/>
      <g class="icon">
        <circle cx="328" cy="466" r="24"/>
        <circle cx="311" cy="451" r="9"/><circle cx="345" cy="446" r="9"/><circle cx="333" cy="480" r="9"/>
      </g>
    </a>
    <a class="step-link" href="#approving-excursion" aria-label="Approving excursion">
      <circle cx="501" cy="462" r="68" fill="var(--pink)"/>
      <circle cx="501" cy="462" r="53" fill="url(#fill-pink)"/>
      <g class="icon">
        <circle cx="501" cy="450" r="17"/>
        <rect x="472" y="460" width="58" height="26" rx="5"/>
        <circle cx="484" cy="488" r="5"/><circle cx="518" cy="488" r="5"/>
      </g>
    </a>
    <a class="step-link" href="#school-manages-excursion" aria-label="School manages the excursion">
      <circle cx="674" cy="462" r="68" fill="var(--blue)"/>
      <circle cx="674" cy="462" r="53" fill="url(#fill-blue)"/>
      <g class="icon">
        <circle cx="674" cy="450" r="11"/><path d="M656 488 v-14 a18 14 0 0 1 36 0 v14"/>
        <circle cx="651" cy="463" r="7"/><path d="M641 488 v-8 a10 9 0 0 1 20 0"/>
        <circle cx="697" cy="463" r="7"/><path d="M687 480 a10 9 0 0 1 20 0 v8"/>
      </g>
    </a>
    <a class="step-link" href="#school-conducts-activity" aria-label="School conducts activity">
      <circle cx="847" cy="462" r="68" fill="var(--purple)"/>
      <circle cx="847" cy="462" r="53" fill="url(#fill-purple)"/>
      <g class="icon">
        <rect x="821" y="437" width="52" height="30" rx="6"/>
        <circle cx="826" cy="478" r="4"/><circle cx="840" cy="478" r="4"/><circle cx="854" cy="478" r="4"/><circle cx="868" cy="478" r="4"/>
        <path d="M821 490 v-5 h10 v5 M835 490 v-5 h10 v5 M849 490 v-5 h10 v5 M863 490 v-5 h10 v5"/>
      </g>
    </a>
    <a class="step-link" href="#students-return" aria-label="Students return to school">
      <circle cx="1020" cy="462" r="68" fill="var(--cyan)"/>
      <circle cx="1020" cy="462" r="53" fill="url(#fill-cyan)"/>
      <g class="icon">
        <path d="M992 488 h56 M996 488 v-24 h48 v24 M1000 464 l20 -16 l20 16"/>
        <circle cx="1020" cy="462" r="5"/>
        <path d="M1020 448 v-12 h9 l-3 3 l3 3 h-9"/>
        <rect x="1014" y="476" width="12" height="12"/>
        <path d="M1000 472 h8 M1000 480 h8 M1032 472 h8 M1032 480 h8"/>
      </g>
    </a>
  </svg>

  <a class="step-label step-label--parent" href="#parent-information">PARENT INFORMATION</a>
  <a class="step-label step-label--student" href="#student-information">STUDENT INFORMATION</a>
  <a class="step-label step-label--approve" href="#approving-excursion">APPROVING EXCURSION</a>
  <a class="step-label step-label--manage" href="#school-manages-excursion">SCHOOL MANAGES THE<br>EXCURSION</a>
  <a class="step-label step-label--conduct" href="#school-conducts-activity">SCHOOL CONDUCTS<br>ACTIVITY</a>
  <a class="step-label step-label--return" href="#students-return">STUDENTS RETURN TO<br>SCHOOL</a>
</main>
</body>
</html>
```